依頼詳細
瓶の容量は330mlで、茶色の瓶で、王冠はシルバーです。(瓶の写真を添付します)
アルコール度数は7%で非加熱処理なので、ドライですっきりとした飲み口のシードルです。
食中酒としてもご利用いただけます。
販売価格は650円(税込み)です。

弊社店舗のロゴも添付しますのでラベルデザインにおいてご活用ください。
また記載いただきたい文字情報として以下の情報をお取り扱いください。

商品名:Marlow CIDER
その他1:The Original Craft & Draft Hard Cider Alc.7%
その他2:APPLE 100% natural
その他2:Harvested and Brewed in HIROSAKI,AOMORI,JAPAN

記載項目
ラベルサイズは縦8センチ×横7センチくらいをを基準にご提案ください。
希望イメージ
シンプル 複雑
単色 カラフル
暗い 明るい
日常 高級
遊び心 厳粛
未来的 伝統的
女性的 男性的
希望する色
茶系
納品ファイル
• 高解像度JPG (.jpg)
• イラストレーター形式 (.ai)

視認性も非常によく、シードルの爽やかな印象をデザインに投影いただきました。

皆様、この度はたくさんのご提案まことにありがとうございます。
心より御礼申し上げます。

```html
<!DOCTYPE html>
<html lang="en">
<head>
<meta charset="utf-8">
<title>Marlow CIDER — Bottle Label</title>
<link href="https://fonts.googleapis.com/css2?family=Roboto+Condensed:wght@400;700;800&display=swap" rel="stylesheet">
<style>
  :root {
    --bg: #eeedea;
    --label: #ffffff;
    --brown: #4e3426;
    --tan: #eddcb9;
    --amber: #c98a2e;
    --art-red: #d8493f;
    --art-glow: #f6e3c4;
  }
  * { margin: 0; padding: 0; box-sizing: border-box; }
  html, body {
    width: 1200px; height: 2712px; overflow: hidden;
    background: var(--bg);
    font-family: "Roboto Condensed", "Arial Narrow", sans-serif;
    color: var(--brown);
  }
  .label {
    position: absolute;
    left: 100px; top: 896px;
    width: 1000px; height: 920px;
    background: var(--label);
    border-radius: 44px;
    box-shadow: 0 6px 24px rgba(0,0,0,0.08);
    text-align: center;
  }
  .tagline-ribbon {
    position: absolute; left: 50%; top: 40px;
    transform: translateX(-50%);
    width: 440px; height: 68px;
  }
  .tagline-ribbon svg { position: absolute; inset: 0; }
  .tagline-text {
    position: relative;
    line-height: 68px;
    font-size: 34px; font-weight: 700;
    letter-spacing: 2px;
    color: var(--amber);
  }
  .cider-art {
    position: absolute; left: 50%; top: 150px;
    transform: translateX(-50%);
    width: 300px; height: 330px;
    border-radius: 50%;
    background: radial-gradient(circle at 50% 38%, var(--art-red) 0 22%, var(--art-glow) 23% 58%, rgba(255,255,255,0) 70%);
  }
  .brand-name {
    position: absolute; left: 0; right: 0; top: 490px;
    font-size: 46px; font-weight: 700; letter-spacing: 2px;
  }
  .product-name {
    position: absolute; left: 0; right: 0; top: 540px;
    font-size: 150px; font-weight: 800; line-height: 1;
    letter-spacing: 6px;
  }
  .product-details {
    position: absolute; left: 0; right: 0; top: 712px;
    font-size: 28px; font-weight: 700; line-height: 44px;
    letter-spacing: 0.5px;
  }
  .shop-mark {
    position: absolute; left: 50%; top: 820px;
    transform: translateX(-50%);
    display: flex; align-items: center; gap: 14px;
    font-size: 40px; font-weight: 700;
  }
  .shop-mark .dot {
    width: 30px; height: 30px; border-radius: 50%;
    background: var(--brown);
  }
</style>
</head>
<body>
  <main class="label">
    <div class="tagline-ribbon">
      <svg viewBox="0 0 440 68" width="440" height="68" aria-hidden="true">
        <polygon points="0,0 440,0 420,34 440,68 0,68 20,34" fill="var(--tan)"/>
      </svg>
      <p class="tagline-text">APPLE 100% natural</p>
    </div>

    <div class="cider-art" role="img" aria-label="Illustration of a wine glass of cider with a red apple and radiating lines"></div>

    <p class="brand-name">Marlow</p>
    <h1 class="product-name">CIDER</h1>
    <p class="product-details">
      The Original Craft &amp; Draft Hard Cider Alc.7%<br>
      Harvested and Brewed in HIROSAKI,AOMORI,JAPAN
    </p>

    <div class="shop-mark">
      <span class="dot"></span>
      <span>Marlow</span>
    </div>
  </main>
</body>
</html>
```